Q-Rolls Business Card

We are a modern retail clothing store. Established in 1994. I need a presentable card that will amaze vendors when given to them.

Front: Logo in middle
Info Side:

Name: Tomas Velder
Cell: 630-812-4463
Work: 630-917-3384 EXT. 417
Email: Tomas@q-rolls-example.com
Website: www.Q-rolls-example.com

Industry/Entity Type

Business

```html
<!DOCTYPE html>
<html lang="en">
<head>
<meta charset="utf-8">
<title>Q-Rolls Business Card</title>
<link rel="stylesheet" href="https://fonts.googleapis.com/css2?family=Lato:wght@400;700;900&display=swap">
<style>
  :root {
    --stage: #1c1c1c;
    --card: #f4f4f4;
    --card-edge: #e2e2e2;
    --ink: #111111;
    --ink-soft: #555555;
    --rule: #4a4a4a;
    --band: #6b6b6b;
    --map: #d6d6d6;
  }
  * { margin: 0; padding: 0; box-sizing: border-box; }
  html, body {
    width: 1200px; height: 873px; overflow: hidden;
    background: var(--stage);
    font-family: "Lato", Arial, sans-serif;
    color: var(--ink);
  }
  .stage { position: relative; width: 1200px; height: 873px; }
  .card {
    position: absolute;
    width: 520px; height: 297px;
    background: linear-gradient(160deg, #ffffff 0%, var(--card) 60%, var(--card-edge) 100%);
    overflow: hidden;
    box-shadow: 0 18px 40px rgba(0,0,0,.6);
  }
  .card--front { left: 60px; top: 200px; }
  .card--info { left: 620px; top: 376px; }
  .world-map {
    position: absolute;
    background: radial-gradient(ellipse at center, var(--map) 0%, rgba(214,214,214,.5) 55%, rgba(214,214,214,0) 75%);
  }
  .card--front .world-map { left: 90px; top: 50px; width: 340px; height: 190px; }
  .card--info .world-map { left: 110px; top: 60px; width: 340px; height: 180px; }
  .edge-band { position: absolute; left: 0; bottom: 0; width: 520px; height: 24px; }
  .brand { position: absolute; text-align: center; }
  .brand__name {
    display: block;
    font-weight: 900; text-transform: uppercase;
    letter-spacing: 1px; color: var(--ink); line-height: 1;
  }
  .brand__tag {
    display: block; font-weight: 400; color: var(--ink-soft);
    letter-spacing: 2px; margin-top: 4px;
  }
  .card--front .brand { left: 0; width: 520px; top: 96px; }
  .card--front .brand__name { font-size: 54px; }
  .card--front .brand__tag { font-size: 14px; }
  .website {
    position: absolute; left: 0; width: 520px; top: 196px;
    text-align: center; font-weight: 700; font-size: 14px;
  }
  .card--info .brand { left: 150px; width: 220px; top: 26px; }
  .card--info .brand__name { font-size: 34px; }
  .card--info .brand__tag { font-size: 10px; }
  .rule { position: absolute; height: 2px; background: var(--rule); }
  .rule--top { left: 130px; top: 124px; width: 230px; }
  .rule--bottom { left: 26px; top: 200px; width: 200px; }
  .person { position: absolute; right: 28px; top: 90px; text-align: right; }
  .person__name { font-weight: 700; font-size: 14px; }
  .person__role { font-size: 11px; color: var(--ink-soft); margin-top: 2px; }
  .address {
    position: absolute; right: 28px; top: 166px; text-align: right;
    font-weight: 700; font-size: 11px; line-height: 1.6;
  }
  .contact { position: absolute; left: 26px; top: 212px; list-style: none; }
  .contact li {
    display: flex; align-items: center; gap: 10px;
    font-size: 11px; color: var(--ink-soft); height: 20px;
  }
  .contact svg { width: 13px; height: 13px; fill: var(--ink); flex: none; }
</style>
</head>
<body>
<main class="stage">

  <section class="card card--front" aria-label="Card front">
    <div class="world-map" role="img" aria-label="Dotted world map backdrop"></div>
    <div class="brand">
      <span class="brand__name">Q-Rolls</span>
      <span class="brand__tag">Fashion Retailer</span>
    </div>
    <p class="website">www.Q-rolls-example.com</p>
    <svg class="edge-band" viewBox="0 0 520 24" aria-hidden="true">
      <path d="M0 18 H360 C378 18 380 4 398 4 H520 V24 H0 Z" fill="var(--band)"/>
    </svg>
  </section>

  <section class="card card--info" aria-label="Card info side">
    <div class="world-map" role="img" aria-label="Dotted world map backdrop"></div>
    <div class="brand">
      <span class="brand__name">Q-Rolls</span>
      <span class="brand__tag">Fashion Retailer</span>
    </div>
    <div class="rule rule--top"></div>
    <div class="person">
      <p class="person__name">Tomas Velder</p>
      <p class="person__role">Owner / Founder</p>
    </div>
    <address class="address" style="font-style:normal">
      118 Harlow St,<br>Brinley IL 60392, United States
    </address>
    <div class="rule rule--bottom"></div>
    <ul class="contact">
      <li>
        <svg viewBox="0 0 16 16" aria-hidden="true"><path d="M2 5c0-2 2-3 6-3s6 1 6 3v1h-3V5H5v1H2z M4 7h8l2 6H2z"/></svg>
        630-917-3384 EXT. 417
      </li>
      <li>
        <svg viewBox="0 0 16 16" aria-hidden="true"><path d="M4 1h8v14H4z M5.5 2.5v10h5v-10z" fill-rule="evenodd"/></svg>
        630-812-4463
      </li>
      <li>
        <svg viewBox="0 0 16 16" aria-hidden="true"><path d="M1 3h14v10H1z M2 4l6 5 6-5z" fill-rule="evenodd"/></svg>
        Tomas@q-rolls-example.com
      </li>
    </ul>
    <svg class="edge-band" viewBox="0 0 520 24" aria-hidden="true">
      <path d="M0 18 H360 C378 18 380 4 398 4 H520 V24 H0 Z" fill="var(--band)"/>
    </svg>
  </section>

</main>
</body>
</html>
```